Blue Fern.....Business Card Design

I am a life coach with a holistic earthy spiritual approach to coaching. The colours I use are the turquoise green range with three large dots going from lighter to darker as a symbol of progression. The main purpose of the card is give my contact details and to write the appointment time and date on the back My tag line is "positive results with a personal touch" I've attached a template I made myself for my invoices the colour isn't as turquoise as I'd like. I don't like block letters I prefer a softer font but not script. I also like tan colours and beachy themes. After the name Blue Fern...... there are at least five dots before the Life Coaching.

Industry/Entity Type

Business

Contact Information for Business Card

Marian Hollis
42 Wrenfield Road
Harlowe 4812

```html
<!DOCTYPE html>
<html lang="en">
<head>
<meta charset="utf-8">
<title>Blue Fern Business Card</title>
<link href="https://fonts.googleapis.com/css2?family=Sniglet:wght@400&family=Delius&display=swap" rel="stylesheet">
<style>
  :root {
    --page: #eeeeee;
    --card: #fdfbec;
    --ink: #1c1c1c;
    --mint: #7fe3c0;
    --mint-deep: #3dc99b;
    --mint-soft: #c9f1e2;
    --label: #2a2a2a;
  }
  * { box-sizing: border-box; margin: 0; padding: 0; }
  html, body { width: 1200px; height: 776px; overflow: hidden; }
  body {
    background: var(--page);
    font-family: "Delius", sans-serif;
    color: var(--ink);
    position: relative;
  }
  .card {
    position: absolute;
    top: 161px;
    height: 314px;
    background: var(--card);
    box-shadow: 6px 10px 16px rgba(0,0,0,0.22);
  }
  .card--front { left: 51px; width: 517px; }
  .card--back { left: 621px; width: 467px; }
  .side-label {
    position: absolute;
    top: 537px;
    width: 200px;
    text-align: center;
    font-size: 17px;
    color: var(--label);
    letter-spacing: 0.5px;
  }
  .side-label--front { left: 210px; }
  .side-label--back { left: 782px; }

  /* Front */
  .ornament {
    position: absolute;
    left: 318px;
    top: 12px;
    width: 68px;
    height: 120px;
  }
  .brand-name {
    position: absolute;
    left: 112px;
    top: 92px;
    font-family: "Sniglet", sans-serif;
    font-weight: 400;
    font-size: 56px;
    line-height: 1;
    color: var(--ink);
    white-space: nowrap;
  }
  .brand-service {
    position: absolute;
    left: 278px;
    top: 163px;
    font-size: 12px;
    color: var(--mint-deep);
    letter-spacing: 0.6px;
    white-space: nowrap;
  }
  .tagline {
    position: absolute;
    left: 0;
    top: 199px;
    width: 100%;
    padding-right: 52px;
    text-align: center;
    font-size: 10px;
    text-transform: uppercase;
    letter-spacing: 1.2px;
    white-space: nowrap;
  }
  .contact {
    position: absolute;
    left: 57px;
    top: 262px;
    white-space: nowrap;
    display: flex;
    align-items: baseline;
    gap: 16px;
  }
  .contact__name {
    font-size: 16px;
    color: var(--mint-deep);
    text-transform: uppercase;
    letter-spacing: 0.3px;
  }
  .contact__address {
    font-size: 10.5px;
    text-transform: uppercase;
    letter-spacing: 0.8px;
  }

  /* Back */
  .rule-top {
    position: absolute;
    left: 51px;
    top: 90px;
    width: 363px;
    height: 2px;
    background: var(--mint);
  }
  .appointment-title {
    position: absolute;
    left: 0;
    top: 102px;
    width: 100%;
    text-align: center;
    font-size: 9px;
    text-transform: uppercase;
    letter-spacing: 0.8px;
  }
  .day {
    position: absolute;
    top: 141px;
    display: flex;
    align-items: center;
    gap: 6px;
    font-size: 9.5px;
    text-transform: uppercase;
    letter-spacing: 0.4px;
    white-space: nowrap;
  }
  .day__box {
    width: 11px;
    height: 11px;
    border: 1.5px solid var(--mint);
  }
  .ampm {
    position: absolute;
    left: 404px;
    top: 167px;
    font-size: 10px;
    line-height: 17px;
  }
  .write-line {
    position: absolute;
    top: 194px;
    height: 1.5px;
    background: var(--mint);
  }
  .write-line--date { left: 96px; width: 208px; }
  .write-line--time { left: 335px; width: 63px; }
  .at-word {
    position: absolute;
    left: 313px;
    top: 186px;
    font-size: 8px;
    text-transform: uppercase;
  }
  .notice {
    position: absolute;
    left: 0;
    top: 244px;
    width: 100%;
    text-align: center;
    font-size: 10px;
    text-transform: uppercase;
    letter-spacing: 0.3px;
    white-space: nowrap;
  }
  .progress-dots {
    position: absolute;
    left: 204px;
    top: 272px;
    display: flex;
    gap: 23px;
  }
  .progress-dots span {
    width: 4px;
    height: 4px;
    border-radius: 50%;
    background: var(--mint);
  }
</style>
</head>
<body>

<section class="card card--front" aria-label="Business card front">
  <svg class="ornament" role="img" aria-label="Decorative fern-like swirl motif" viewBox="0 0 68 120" preserveAspectRatio="none">
    <defs>
      <radialGradient id="ornamentTone" cx="50%" cy="55%" r="50%">
        <stop offset="0%" stop-color="#c9f1e2"/>
        <stop offset="100%" stop-color="#c9f1e2" stop-opacity="0"/>
      </radialGradient>
    </defs>
    <rect width="68" height="120" fill="url(#ornamentTone)"/>
  </svg>
  <h1 class="brand-name">BLUE FERN</h1>
  <p class="brand-service">LIFE COACHING</p>
  <p class="tagline">~ Positive results with a personal touch ~</p>
  <p class="contact">
    <span class="contact__name">Marian Hollis</span>
    <span class="contact__address">42 Wrenfield Road Harlowe 4812</span>
  </p>
</section>

<section class="card card--back" aria-label="Business card back">
  <div class="rule-top"></div>
  <p class="appointment-title">Has an appointment on</p>
  <span class="day" style="left:86px"><span class="day__box"></span>Mon.</span>
  <span class="day" style="left:161px"><span class="day__box"></span>Tues.</span>
  <span class="day" style="left:235px"><span class="day__box"></span>Wed.</span>
  <span class="day" style="left:314px"><span class="day__box"></span>Thurs.</span>
  <span class="day" style="left:398px"><span class="day__box"></span>Fri.</span>
  <p class="ampm">A.M.<br>P.M.</p>
  <div class="write-line write-line--date"></div>
  <span class="at-word">at</span>
  <div class="write-line write-line--time"></div>
  <p class="notice">If unable to keep appointment kindly give 24 hours notice.</p>
  <div class="progress-dots"><span></span><span></span><span></span><span></span></div>
</section>

<p class="side-label side-label--front">FRONT</p>
<p class="side-label side-label--back">BACK</p>

</body>
</html>
```